Clinical Layout Builders - Stationery
Biz Cards + Stationary
Clinical Layout Builders - Stationery - Information Technology
Creative Brief
Professional
Dr. Elena M. Castillo
Director of Content Development
Ceiba Business Plaza #3, Suite 118 San Juan, PR 00941
(787) PENDING
elena.castillo@hnvwqbt.com
www.hnvwqbt.com
Need a second set of cards for: Dr. Luis F. Beltran Business Development Director Same info- address, fax and phone (Pending) Cell: (787) 555-0192 Email: luis.beltran@hnvwqbt.com
Either the logo, the website or something else. Feel free to be creative!

```html
<!DOCTYPE html>
<html lang="en">
<head>
<meta charset="utf-8">
<title>Clinical Layout Builders – Stationery</title>
<link href="https://fonts.googleapis.com/css2?family=Roboto:wght@400;700&display=swap" rel="stylesheet">
<style>
  :root {
    --backdrop: #c9c9c9;
    --paper: #ffffff;
    --band: #363233;
    --brand: #c9558e;
    --ink: #333333;
    --muted: #a8a8a8;
    --card-ink: #dcdcdc;
    --swoosh: #e9c9dc;
  }
  * { box-sizing: border-box; margin: 0; padding: 0; }
  html, body { width: 1200px; height: 684px; overflow: hidden; }
  body {
    background: var(--backdrop);
    font-family: "Roboto", Arial, sans-serif;
    color: var(--ink);
    position: relative;
  }
  .sheet {
    position: absolute;
    z-index: 1;
    background: var(--paper);
    box-shadow: 0 1px 3px rgba(0,0,0,.25);
    overflow: hidden;
  }
  .band { position: absolute; left: 0; right: 0; top: 0; background: var(--band); }
  .brand {
    position: absolute;
    display: flex; align-items: center; gap: 6px;
    color: var(--brand);
    font-weight: 700;
    white-space: nowrap;
    letter-spacing: .02em;
  }
  .brand-dot { border-radius: 50%; background: var(--brand); flex: none; }
  .contact {
    position: absolute;
    font-size: 7px; line-height: 10px;
    color: var(--ink);
    white-space: nowrap;
  }
  .contact b { font-weight: 700; }
  .swoosh {
    position: absolute;
    border-radius: 50%;
    background: radial-gradient(ellipse at center, var(--swoosh) 0%, rgba(233,201,220,.6) 55%, rgba(255,255,255,0) 72%);
  }
  .web { position: absolute; font-size: 7px; color: var(--ink); }

  /* Letterhead */
  .letterhead { left: 96px; top: 34px; width: 473px; height: 619px; }
  .letterhead .band { height: 110px; }
  .letterhead .brand { left: 24px; top: 38px; font-size: 17px; }
  .letterhead .brand-dot { width: 14px; height: 14px; }
  .letterhead .contact { left: 24px; top: 570px; z-index: 1; }
  .letterhead .swoosh { left: 70px; top: 588px; width: 340px; height: 40px; }

  /* Envelope back */
  .envelope-back { left: 576px; top: 67px; width: 528px; height: 233px; }
  .envelope-back svg { position: absolute; left: 0; top: 0; }
  .envelope-back .brand { left: 0; right: 0; justify-content: center; top: 74px; font-size: 17px; }
  .envelope-back .brand-dot { width: 14px; height: 14px; }

  /* Envelope front */
  .envelope-front { left: 576px; top: 312px; width: 528px; height: 228px; }
  .envelope-front .band { height: 65px; }
  .envelope-front .brand { left: 20px; top: 22px; font-size: 17px; }
  .envelope-front .brand-dot { width: 14px; height: 14px; }
  .envelope-front .contact { left: 20px; top: 166px; z-index: 1; }
  .envelope-front .web { right: 22px; top: 180px; }
  .envelope-front .swoosh { left: 100px; top: 188px; width: 360px; height: 34px; }

  /* Business cards (sit on top of the letterhead) */
  .card {
    position: absolute; z-index: 2; left: 8px; width: 200px; height: 111px;
    background: var(--band);
    box-shadow: 0 1px 4px rgba(0,0,0,.4);
    color: var(--card-ink);
    overflow: hidden;
  }
  .card-front { top: 230px; }
  .card-back { top: 346px; }
  .card .name {
    position: absolute; left: 9px; top: 7px;
    font-size: 5.5px; font-weight: 700; white-space: nowrap; color: #eeeeee;
  }
  .card .name span { font-weight: 400; color: var(--muted); }
  .card .brand { left: 9px; top: 24px; font-size: 11px; }
  .card .brand-dot { width: 9px; height: 9px; }
  .card .details {
    position: absolute; left: 9px; top: 68px;
    font-size: 5.5px; line-height: 8px; white-space: nowrap;
  }
  .card .details b { font-weight: 700; }
  .card .card-web { position: absolute; left: 10px; bottom: 10px; font-size: 7px; font-weight: 700; color: #f0f0f0; }
</style>
</head>
<body>

  <section class="sheet letterhead">
    <div class="band"></div>
    <div class="brand"><span class="brand-dot"></span>Clinical Layout Builders</div>
    <p class="contact">
      <b>Email:</b> elena.castillo@hnvwqbt.com<br>
      <b>Phone:</b> (787) PENDING | <b>Fax:</b> (787) PENDING<br>
      <b>Address:</b> Ceiba Business Plaza #3, Suite 118, San Juan, PR 00941
    </p>
    <div class="swoosh"></div>
  </section>

  <section class="sheet envelope-back">
    <svg width="528" height="233" viewBox="0 0 528 233" aria-hidden="true">
      <path d="M0 0 H528 V118 Q400 125 300 160 Q264 172 228 160 Q128 125 0 118 Z" fill="var(--band)"/>
    </svg>
    <div class="brand"><span class="brand-dot"></span>Clinical Layout Builders</div>
  </section>

  <section class="sheet envelope-front">
    <div class="band"></div>
    <div class="brand"><span class="brand-dot"></span>Clinical Layout Builders</div>
    <p class="contact">
      <b>Email:</b> elena.castillo@hnvwqbt.com<br>
      <b>Phone:</b> (787) PENDING | <b>Fax:</b> (787) PENDING<br>
      <b>Address:</b> Ceiba Business Plaza #3, Suite 118, San Juan, PR 00941
    </p>
    <p class="web">www.hnvwqbt.com</p>
    <div class="swoosh"></div>
  </section>

  <section class="card card-front">
    <p class="name">Dr. Elena M. Castillo <span>· Director of Content Development</span></p>
    <div class="brand"><span class="brand-dot"></span>Clinical Layout Builders</div>
    <p class="details">
      <b>Email:</b> elena.castillo@hnvwqbt.com<br>
      <b>Phone:</b> (787) PENDING | <b>Fax:</b> (787) PENDING<br>
      Ceiba Business Plaza #3, Suite 118, San Juan, PR 00941
    </p>
  </section>

  <section class="card card-back">
    <div class="brand" style="top:20px"><span class="brand-dot"></span>Clinical Layout Builders</div>
    <p class="card-web">www.hnvwqbt.com</p>
  </section>

</body>
</html>
```